3D abstract logo Construction, Kitchen and Bath design and Project Management Business Card Design

I want a 3d abstract logo for a new General Construction, Kitchen and Bath design and Project Management Company located at Philadelphia PA, we want to put our logo in the white color trucks too. I want to look professional and serious at the same time look like an architect design and the warm originals color that make you feel in a nice decorated home, I like the colors trend in this link:
http://www.quillorbit.example/qo/kts/cardmaker.aspx?alt_doc_id=RM41T-K7B93-2W5&doc_id=5130948826&pf_id=H4D

I was thinking about a roof and the PA font could have square shape or like wood framing with two tones of the brick color black and creamy yellow color.... Also I like the keystone Idea like the modification or the LK Skyroute logo but curvy at the top

The final design should communicate big company (because we want to grow), responsible, professional and organized that really care about our customers and give them everything they need... plan and design, excellent labor and Project Management
Updates

I doesn't have to be 3d

Reason: I haven't received enough options...

Please stick with the warm tones shown in the image001 attached I like spicy cinnamon instead a cold wine or brick color and also the cream yellowish tones added

Hello designers, please use only the idea and colors of the image001 I don't want to be stick with a house logo because I do commercial construction too so I prefer work around the keystone idea maybe leaving the style of the PA.
I'd like the base tone on the card dark like first option and you can send me a white option too.

Please send me your ideas as soon as possible 

Thank you so much!

Target Market(s)

Builders, State, commercial business owners, Property owners or Real State and Property Management Companies

Industry/Entity Type

Architect

Contact Information for Business Card

LK Buildworks LLC
“Your project is our business”
Renata Solvik Eng.
President
Commercial & Residential General Construction
Kitchen & Bath Design | Project Management
Phone: 215-738-4196 | Fax: 215-738-4197 Cell: 856-390-7712
renata@lkbuildworks.example

```html
<!DOCTYPE html>
<html lang="en">
<head>
<meta charset="utf-8">
<title>LK Buildworks – Business Cards</title>
<link rel="stylesheet" href="https://fonts.googleapis.com/css2?family=Arimo:ital,wght@0,400;0,700;1,400&family=Ubuntu:wght@400&display=swap">
<style>
  :root {
    --cinnamon: #a81e2a;
    --cinnamon-warm: #c0392e;
    --cream: #fdf9e9;
    --paper: #ffffff;
    --ink: #1c1c1c;
    --service: #d0503f;
    --web-faint: #d9584f;
  }
  * { margin: 0; padding: 0; box-sizing: border-box; }
  html, body { width: 1200px; height: 900px; overflow: hidden; background: var(--paper); }
  .sheet { position: relative; width: 1200px; height: 900px; font-family: "Arimo", Arial, sans-serif; }

  .card { position: absolute; overflow: hidden; }
  .card--front { width: 528px; height: 310px; background: var(--cream); }
  .card--front-light { left: 28px; top: 22px; }
  .card--front-dark { left: 636px; top: 19px; }

  .card__accent {
    position: absolute; right: 0; top: 0; width: 84px; height: 100%;
    background: linear-gradient(180deg, var(--cinnamon) 0%, var(--cinnamon-warm) 100%);
  }

  .card__name { position: absolute; left: 26px; top: 22px; font-size: 30px; font-weight: 700; color: var(--cinnamon); letter-spacing: 0.2px; }
  .card__title { position: absolute; left: 27px; top: 59px; font-size: 19px; font-style: italic; color: var(--cinnamon); }
  .card__services { position: absolute; left: 26px; top: 99px; font-family: "Ubuntu", sans-serif; font-size: 18.5px; line-height: 21px; color: var(--service); }

  .contact { position: absolute; left: 26px; top: 203px; font-size: 14px; line-height: 23px; }
  .contact__row { display: flex; }
  .contact__label { width: 73px; color: var(--cinnamon); }
  .contact__value { color: var(--ink); }

  .badge { position: absolute; width: 104px; height: 104px; border-radius: 50%; display: flex; align-items: center; justify-content: center; text-align: center; font-size: 13px; font-weight: 700; line-height: 15px; }
  .card--front-light .badge { left: 386px; top: 188px; background: var(--cream); color: var(--cinnamon); }
  .card--front-dark .badge { left: 382px; top: 179px; background: var(--cinnamon); color: var(--cream); }

  .card--back { width: 310px; height: 528px; text-align: center; }
  .card--back-light { left: 125px; top: 348px; background: var(--cream); color: var(--cinnamon); }
  .card--back-dark { left: 733px; top: 363px; background: var(--cinnamon); color: var(--cream); }
  .card__brand { position: absolute; left: 0; right: 0; top: 270px; font-size: 27px; font-weight: 700; }
  .card__tagline { position: absolute; left: 0; right: 0; top: 346px; font-size: 16.5px; }
  .card__web { position: absolute; left: 0; right: 0; top: 451px; font-size: 13px; }
  .card--back-dark .card__brand { top: 258px; }
  .card--back-dark .card__tagline { top: 330px; }
  .card--back-dark .card__web { top: 451px; color: var(--web-faint); }
</style>
</head>
<body>
<main class="sheet">

  <section class="card card--front card--front-light">
    <div class="card__accent" role="img" aria-label="Decorative warm swoosh band"></div>
    <h1 class="card__name">RENATA SOLVIK</h1>
    <p class="card__title">Eng. President</p>
    <p class="card__services">Commercial &amp; Residential General<br>Construction Kitchen &amp; Bath Design</p>
    <div class="contact">
      <div class="contact__row"><span class="contact__label">Phone:</span><span class="contact__value">215-738-4196</span></div>
      <div class="contact__row"><span class="contact__label">Fax:</span><span class="contact__value">215-738-4197</span></div>
      <div class="contact__row"><span class="contact__label">Cell:</span><span class="contact__value">856-390-7712</span></div>
      <div class="contact__row"><span class="contact__label">Email:</span><span class="contact__value">renata@lkbuildworks.example</span></div>
    </div>
    <div class="badge">LK<br>Buildworks</div>
  </section>

  <section class="card card--front card--front-dark">
    <div class="card__accent" role="img" aria-label="Decorative warm swoosh band"></div>
    <h1 class="card__name">RENATA SOLVIK</h1>
    <p class="card__title">Eng. President</p>
    <p class="card__services">Commercial &amp; Residential General<br>Construction Kitchen &amp; Bath Design</p>
    <div class="contact">
      <div class="contact__row"><span class="contact__label">Phone:</span><span class="contact__value">215-738-4196</span></div>
      <div class="contact__row"><span class="contact__label">Fax:</span><span class="contact__value">215-738-4197</span></div>
      <div class="contact__row"><span class="contact__label">Cell:</span><span class="contact__value">856-390-7712</span></div>
      <div class="contact__row"><span class="contact__label">Email:</span><span class="contact__value">renata@lkbuildworks.example</span></div>
    </div>
    <div class="badge">LK<br>Buildworks</div>
  </section>

  <section class="card card--back card--back-light">
    <p class="card__brand">LK Buildworks</p>
    <p class="card__tagline">Your project is our business</p>
    <p class="card__web">www.lkbuildworks.example</p>
  </section>

  <section class="card card--back card--back-dark">
    <p class="card__brand">LK Buildworks</p>
    <p class="card__tagline">Your project is our business</p>
    <p class="card__web">www.lkbuildworks.example</p>
  </section>

</main>
</body>
</html>
```